Freelance business trainer needs a new business card

My business is called Tbrite. I provide training in the workplace on management, coaching and mentoring, and customer service topics for a variety of businesses, colleges and private training providers, and teach on management programs. I need a professional but eye catching business card. Business colours grey and orange. My name Linda Marchbank; Tel 07853 416207; email lmarchbank@tbrite.co.uk; website www.tbrite.co.uk.
Happy to have some sort of logo on front and details on back or all on one side
Target Market(s)
SME businesses and colleges - workshops i run are for adults in the workplace
Industry/Entity Type
Training
Look and feel

```html
<!DOCTYPE html>
<html lang="en">
<head>
<meta charset="utf-8">
<title>Tbrite – Business Card</title>
<link rel="stylesheet" href="https://fonts.googleapis.com/css2?family=Jost:wght@400&display=swap">
<style>
  :root {
    --brand-orange: #df762d;
    --brand-grey: #717476;
    --rule-grey: #a8a9ab;
    --ink: #231f20;
    --paper: #ffffff;
    --border: #b9b9b9;
  }
  * { margin: 0; padding: 0; box-sizing: border-box; }
  html, body {
    width: 953px;
    height: 1200px;
    overflow: hidden;
    background: var(--paper);
    font-family: "Jost", "Futura", sans-serif;
  }
  .canvas {
    position: relative;
    width: 953px;
    height: 1200px;
  }
  .card { position: absolute; left: 0; width: 953px; }
  .card--front {
    top: 0;
    height: 581px;
    background: var(--brand-orange);
  }
  .card--back {
    top: 617px;
    height: 582px;
    background: var(--paper);
    border: 1px solid var(--border);
  }
  .wordmark {
    position: absolute;
    display: flex;
    align-items: center;
    gap: 14px;
    font-weight: 400;
    letter-spacing: 0.06em;
    text-transform: uppercase;
    line-height: 1;
  }
  .wordmark__dot { border-radius: 50%; flex: none; }
  .wordmark--front {
    left: 50%;
    top: 286px;
    transform: translate(-50%, -50%);
    font-size: 76px;
    color: var(--paper);
  }
  .wordmark--front .wordmark__dot {
    width: 84px; height: 84px;
    background: var(--brand-grey);
  }
  .wordmark--back {
    left: 74px;
    top: 904px;
    transform: translateY(-50%);
    font-size: 58px;
    color: var(--brand-orange);
    gap: 10px;
  }
  .wordmark--back .wordmark__dot {
    width: 66px; height: 66px;
    background: var(--brand-grey);
  }
  .divider {
    position: absolute;
    left: 470px;
    top: 720px;
    width: 10px;
    height: 376px;
  }
  .contact {
    position: absolute;
    left: 533px;
    top: 792px;
    color: var(--ink);
  }
  .contact__name {
    font-size: 35px;
    font-weight: 400;
    letter-spacing: 0.04em;
    color: var(--brand-orange);
    margin-bottom: 44px;
    line-height: 1.2;
  }
  .contact__list { list-style: none; }
  .contact__item {
    font-size: 24px;
    letter-spacing: 0.02em;
    line-height: 45px;
  }
</style>
</head>
<body>
<div class="canvas">
  <section class="card card--front">
    <div class="wordmark wordmark--front">
      <span class="wordmark__dot"></span>
      <span class="wordmark__name">Tbrite</span>
    </div>
  </section>

  <section class="card card--back">
  </section>

  <div class="wordmark wordmark--back">
    <span class="wordmark__dot"></span>
    <span class="wordmark__name">Tbrite</span>
  </div>

  <svg class="divider" viewBox="0 0 10 376" preserveAspectRatio="none" aria-hidden="true">
    <polygon points="5,0 6.5,188 5,376 3.5,188" fill="var(--rule-grey)"/>
  </svg>

  <div class="contact">
    <h1 class="contact__name">Linda Marchbank</h1>
    <ul class="contact__list">
      <li class="contact__item">07853 416207</li>
      <li class="contact__item">lmarchbank@tbrite.co.uk</li>
      <li class="contact__item">www.tbrite.co.uk.</li>
    </ul>
  </div>
</div>
</body>
</html>
```